依頼詳細
今年の仮チラシをファイル添付しておきますので、講師の肩書、名前等の確認をお願いいたします。

昨年の講演会のチラシもファイル添付しておきますので、参考にお願いいたします。

こどもさんの笑顔の写真や、家族で幸せそうにしている写真がありそうでしたら、多めに使用していただけますか。
記載項目
記載項目は基本2018年のチラシと同じですので、ファイル添付分で確認をおねがいします。(日付だけが、9月21日(土)となります。)
サイズ
A4
ページ数
片面
希望イメージ
シンプル 複雑
単色 カラフル
暗い 明るい
日常 高級
遊び心 厳粛
未来的 伝統的
女性的 男性的
希望する色
水色系、緑系、黄・オレンジ系
納品ファイル
• 高解像度JPG (.jpg)
補足説明
今年の講演会チラシにも講師二人の写真を入れる予定です。撮影できしだいファイルをおくるかたちとなります。よろしくお願いいたします。
■ 選んだ理由

イメージと合ったから。

■ 提案者全員のお礼・コメント

みなさん、ご協力ありがとうございました。

```html
<!DOCTYPE html>
<html lang="ja">
<head>
<meta charset="utf-8">
<title>こどもの栄養×こどもの姿勢 講演会</title>
<link href="https://fonts.googleapis.com/css2?family=M+PLUS+Rounded+1c:wght@400;700;800&display=swap" rel="stylesheet">
<style>
:root{
  --bg:#eef8fb;
  --white:#ffffff;
  --orange:#f08a24;
  --orange-light:#f7b44a;
  --green:#5aa83c;
  --green-light:#8cc63f;
  --blue:#3a9fd0;
  --yellow:#f6d34a;
  --ink:#4a4a4a;
  --gray:#9a9a9a;
}
*{margin:0;padding:0;box-sizing:border-box}
html,body{width:854px;height:1200px;overflow:hidden}
body{font-family:"M PLUS Rounded 1c",sans-serif;color:var(--ink);background:var(--bg);position:relative}
.photo{position:absolute;border-radius:6px}
.photo--warm{background:linear-gradient(135deg,#f6e3cf,#e9c9a8)}
.photo--cool{background:linear-gradient(135deg,#d9ecf3,#b9d9e6)}
.photo--green{background:linear-gradient(135deg,#e3f0d4,#c3dfa8)}
.tableware{position:absolute;left:117px;top:40px;width:620px;height:600px;border-radius:50%;background:radial-gradient(circle at 50% 48%,#ffffff 0%,#ffffff 70%,#f1f3f4 86%,#e6e9eb 100%);box-shadow:0 4px 18px rgba(0,0,0,.10)}
.tagline{position:absolute;left:287px;top:118px;width:280px;height:34px;border-radius:17px;background:var(--yellow);color:#6a4a10;font-size:17px;font-weight:700;text-align:center;line-height:34px}
.title{position:absolute;left:137px;top:165px;width:580px;text-align:center}
.title__small{display:flex;justify-content:center;gap:180px;font-size:32px;font-weight:800}
.title__small span:first-child{color:var(--orange)}
.title__small span:last-child{color:var(--green)}
.title__main{font-size:104px;font-weight:800;line-height:1.05;letter-spacing:2px}
.title__main .nutrition{color:var(--orange)}
.title__main .cross{color:var(--gray);font-size:70px;margin:0 8px;vertical-align:12px}
.title__main .posture{color:var(--green)}
.lead{position:absolute;left:137px;top:392px;width:580px;text-align:center;font-weight:700}
.lead__line1{font-size:27px;color:var(--green)}
.lead__line2{font-size:34px;color:var(--blue);margin-top:4px}
.speakers{position:absolute;left:16px;top:668px;width:822px;display:flex;gap:14px}
.speaker{flex:1;height:228px;background:var(--white);border:3px solid var(--green-light);border-radius:12px;padding:14px 16px;position:relative}
.speaker--right{border-color:var(--blue)}
.speaker__role{font-size:14px;color:var(--green);font-weight:700}
.speaker--right .speaker__role{color:var(--blue)}
.speaker__name{font-size:26px;font-weight:800;margin-top:2px}
.speaker__name small{font-size:14px;margin-left:4px}
.speaker__photo{position:absolute;right:16px;top:12px;width:110px;height:64px;background:#d9d9d9;color:#fff;font-size:20px;font-weight:700;display:flex;align-items:center;justify-content:center}
.speaker__list{list-style:none;margin-top:26px;font-size:13px;line-height:1.9}
.speaker__list li::before{content:"●";color:var(--orange-light);margin-right:6px;font-size:10px}
.info{position:absolute;left:16px;top:906px;width:822px}
.info__row{display:flex;align-items:center;gap:12px}
.label{display:inline-block;background:var(--blue);color:#fff;font-size:15px;font-weight:700;padding:4px 12px;border-radius:4px}
.date{font-size:15px}
.date__big{font-size:70px;font-weight:800;color:var(--blue);line-height:1}
.date__dow{display:inline-block;background:var(--orange);color:#fff;border-radius:50%;width:38px;height:38px;text-align:center;line-height:38px;font-size:20px;font-weight:800;vertical-align:10px}
.times{font-size:16px;line-height:1.5}
.fee{position:absolute;left:512px;top:0;display:flex;align-items:center;gap:10px}
.fee__price{font-size:30px;font-weight:800;color:var(--orange)}
.note{position:absolute;left:700px;top:0;font-size:11px;line-height:1.5;width:124px}
.venue{margin-top:8px}
.venue__name{font-size:20px;font-weight:700}
.venue__addr{font-size:13px;line-height:1.5}
.host{position:absolute;left:512px;top:74px;font-size:14px;line-height:1.6}
.host__tel{font-size:20px;font-weight:800;color:var(--blue)}
.map{position:absolute;left:16px;top:1072px;width:236px;height:116px;background:linear-gradient(135deg,#e4e4e4,#cfcfcf);color:#fff;font-size:26px;font-weight:700;display:flex;align-items:center;justify-content:center}
.memo{position:absolute;left:560px;top:1150px;width:278px;height:38px;background:var(--white);border:1px solid #ccc;font-size:11px;padding:4px 8px}
</style>
</head>
<body>
  <div class="photo photo--warm" style="left:0;top:0;width:250px;height:200px" role="img" aria-label="笑顔のこどもたちの写真"></div>
  <div class="photo photo--cool" style="left:260px;top:0;width:330px;height:110px" role="img" aria-label="家族で楽しそうに過ごす写真"></div>
  <div class="photo photo--green" style="left:600px;top:0;width:254px;height:200px" role="img" aria-label="食事をするこどもの写真"></div>
  <div class="photo photo--warm" style="left:10px;top:470px;width:190px;height:170px" role="img" aria-label="元気に遊ぶこどもの写真"></div>
  <div class="photo photo--cool" style="left:654px;top:470px;width:190px;height:170px" role="img" aria-label="姿勢よく座るこどもの写真"></div>

  <div class="tableware" role="img" aria-label="お皿とナイフ・フォークのイラスト"></div>
  <div class="tagline">こども達の輝かしい未来のために！</div>
  <div class="title">
    <div class="title__small"><span>こどもの</span><span>こどもの</span></div>
    <div class="title__main"><span class="nutrition">栄養</span><span class="cross">×</span><span class="posture">姿勢</span></div>
  </div>
  <div class="lead">
    <div class="lead__line1">こどもの栄養専門家と健康科学博士による</div>
    <div class="lead__line2">コラボレーション講演会</div>
  </div>

  <section class="speakers">
    <div class="speaker">
      <div class="speaker__role">管理栄養士</div>
      <div class="speaker__name">山川 真弓<small>氏</small></div>
      <div class="speaker__photo">photo</div>
      <ul class="speaker__list">
        <li>毎日の食事で気をつけたいポイント</li>
        <li>好き嫌いを減らすための工夫とは？</li>
        <li>成長期に必要な栄養をバランスよく</li>
        <li>家族で楽しむ食卓づくりのヒント</li>
      </ul>
    </div>
    <div class="speaker speaker--right">
      <div class="speaker__role">健康科学博士</div>
      <div class="speaker__name">高原 誠司<small>氏</small></div>
      <div class="speaker__photo">photo</div>
      <ul class="speaker__list">
        <li>こどもの姿勢はなぜ崩れるのか？</li>
        <li>正しい座り方と立ち方の基本</li>
        <li>毎日できるかんたん姿勢体操</li>
        <li>姿勢と集中力の深い関係</li>
      </ul>
    </div>
  </section>

  <section class="info">
    <div class="info__row">
      <span class="label">日時</span>
      <span class="date">令和元年</span>
      <span class="date__big">9/21</span><span class="date__dow">土</span>
      <div class="times">開場 13:00<br>開演 13:30</div>
    </div>
    <div class="fee"><span class="label">参加費</span><span class="fee__price">4000円</span></div>
    <div class="note">参加費は当日受付にてお支払いください</div>
    <div class="venue info__row">
      <span class="label">会場</span>
      <div>
        <div class="venue__name">市民文化プラザ 2階ホール</div>
        <div class="venue__addr">〒600-0000<br>みどり市中央区さくら通1-2-3</div>
      </div>
    </div>
    <div class="host">
      <span class="label">主催</span> みどり県こども健康協会<br>
      お問い合わせ <span class="host__tel">TEL.000-123-4567</span>
    </div>
  </section>

  <div class="map" role="img" aria-label="会場周辺の地図">map</div>
  <div class="memo">備考</div>
</body>
</html>
```